Food Safety 1-California workers only

3.25" by 4.5" Black and White Magazine Ad
This ad is to train California workers only.
Workers will be trained on: Food Safety, FSMA (Food Safety Modernization Act), using equipment safety, food processing production skills, worker safety, supervisory skills, communication skills.
"FREE TRAINING", The company does the training or Keystone Learning will provide the training.
Training grants range from $100,000 to $400,000.
Companies must be in business for profit.
Companies must train 200 employees or more.
This program is for California workers only.
Incumbent or new-hires are eligible.

Target Market(s)

California food processors, farms, food packaging, food processors, companies under FSMA, food safety, food production who need to train employees.

Industry/Entity Type

Food Production

Font styles to use
Serif
Sans Serif

Colors

Designer to choose colors to be used in the design.

Requirements
Must have
• This is a 3.25 inch by 4.5 inch magazine ad. It must be black and white. No color.
• The deliverable must be in basic PhotoShop. The ad does not need to include any graphics and be text only if needed. If you have a black and white graphic that will show well.
• Look at www.KLGFoodSafety..com
• Use the text from "MEALBOX-Photoshop-052018" file as your starting point.
Nice to have
• A black and white graphic about food. See www.KLGFoodSafety.com
Should not have
• No color.

```html
<!DOCTYPE html>
<html lang="en">
<head>
<meta charset="utf-8">
<title>Free Training Ad</title>
<link href="https://fonts.googleapis.com/css2?family=Lato:wght@400;700;900&display=swap" rel="stylesheet">
<style>
  :root{
    --black:#0d0d0d;
    --ink:#1a1a1a;
    --charcoal:#333333;
    --panel:#dcdcdc;
    --page:#e9e9e9;
    --white:#ffffff;
    --text:#222222;
    --rule:#6a6a6a;
  }
  *{margin:0;padding:0;box-sizing:border-box}
  html,body{width:1200px;height:1200px;overflow:hidden;background:var(--page)}
  body{font-family:"Lato",sans-serif;position:relative}
  .ad{
    position:absolute;left:181px;top:20px;width:906px;height:1255px;
    transform:scale(0.924);transform-origin:0 0;
    background:var(--white);box-shadow:0 6px 16px rgba(0,0,0,.25);overflow:hidden
  }
  .header{position:absolute;left:0;top:0;width:906px;height:205px;background:var(--black);text-align:center;color:var(--white)}
  .header h1{font-weight:900;font-size:70px;letter-spacing:1px;padding-top:38px;line-height:1}
  .header .topics{font-size:24px;font-weight:400;margin-top:32px;letter-spacing:.3px}
  .hero{
    position:absolute;left:0;top:205px;width:906px;height:470px;
    background:linear-gradient(100deg,#8a8a8a 0%,#d2d2d2 25%,#bdbdbd 45%,#9a9a9a 65%,#4a4a4a 82%,#8c8c8c 100%);
    clip-path:polygon(0 0,100% 0,100% 96%,0 100%)
  }
  .quote{
    position:absolute;left:0;top:483px;width:565px;height:164px;background:var(--ink);
    color:var(--white);padding:20px 0 0 56px;font-size:31px;line-height:40px;font-weight:400;text-transform:uppercase
  }
  .quote strong{font-weight:700}
  .qualify-bar{position:absolute;left:0;top:660px;width:906px;height:112px;background:var(--charcoal)}
  .qualify-bar h2{position:absolute;left:56px;top:66px;color:var(--panel);font-size:26px;font-weight:700;letter-spacing:.3px}
  .criteria{position:absolute;left:0;top:772px;width:906px;height:246px;background:var(--panel);color:var(--text);font-size:22px}
  .criteria ul{position:absolute;list-style:none}
  .criteria li{position:relative;padding-left:24px}
  .criteria li::before{content:"";position:absolute;left:0;top:13px;width:6px;height:6px;border-radius:50%;background:var(--text)}
  .col-left{left:56px;top:36px}
  .col-left li{height:39px;line-height:28px}
  .col-right{left:489px;top:34px;width:380px}
  .col-right li{line-height:28px;margin-bottom:10px}
  .divider{position:absolute;left:449px;top:25px;width:1px;height:198px;background:var(--rule)}
  .footer{position:absolute;left:0;top:1018px;width:906px;height:237px;background:var(--black);color:var(--white);font-size:22px}
  .footer .tail{position:absolute;left:0;bottom:0;width:906px;height:30px;background:#cfcfcf;clip-path:polygon(0 20%,100% 55%,100% 100%,0 100%)}
  .contact{position:absolute;left:60px;top:38px;list-style:none}
  .contact li{display:flex;align-items:center;height:38px}
  .contact svg{width:22px;height:22px;margin-right:17px;fill:none;stroke:var(--white);stroke-width:1.8}
  .address{position:absolute;left:480px;top:66px;display:flex}
  .address svg{width:28px;height:34px;margin-right:16px;margin-top:30px;fill:none;stroke:var(--white);stroke-width:2}
  .address p{line-height:28px}
</style>
</head>
<body>
  <article class="ad">
    <header class="header">
      <h1>FREE TRAINING</h1>
      <p class="topics">FOOD SAFETY | FSMA | PRODUCTION SKILLS | &nbsp;WORKER SAFETY</p>
    </header>

    <div class="hero" role="img" aria-label="Black and white photo of chefs in white hats being trained in a commercial kitchen"></div>

    <blockquote class="quote">&ldquo;You do the<br>training and <strong>the state<br>of California pays for it!&rdquo;</strong></blockquote>

    <section class="qualify-bar"><h2>HOW TO QUALIFY</h2></section>

    <section class="criteria">
      <ul class="col-left">
        <li>Train California Workers Only</li>
        <li>Trainees must earn $11/hour</li>
        <li>Full-time workers only</li>
        <li>Employees must attend at least 8</li>
        <li>Hours of training</li>
      </ul>
      <div class="divider"></div>
      <ul class="col-right">
        <li>You must train 200 or more employees</li>
        <li>Incumbent or New-Hire workers &nbsp;are eligible</li>
        <li>Seasonal workers are eligible</li>
      </ul>
    </section>

    <footer class="footer">
      <ul class="contact">
        <li><svg viewBox="0 0 24 24"><path d="M5 3l4 1 1 5-3 2a12 12 0 0 0 6 6l2-3 5 1 1 4-2 2C10 21 3 14 3 5z"/></svg>(555) 014-3200</li>
        <li><svg viewBox="0 0 24 24"><rect x="3" y="6" width="18" height="12"/><path d="M3 6l9 7 9-7"/></svg>Dan.Moreno@KLGCAL.com</li>
        <li><svg viewBox="0 0 24 24"><circle cx="12" cy="12" r="9"/><path d="M3 12h18M12 3c4 4 4 14 0 18M12 3c-4 4-4 14 0 18"/></svg>www.KLGCAL.com</li>
        <li><svg viewBox="0 0 24 24"><circle cx="12" cy="12" r="9"/><path d="M3 12h18M12 3c4 4 4 14 0 18M12 3c-4 4-4 14 0 18"/></svg>www.KLGFoodSafety.com</li>
      </ul>
      <div class="address">
        <svg viewBox="0 0 24 30"><path d="M12 28S3 17 3 11a9 9 0 0 1 18 0c0 6-9 17-9 17z"/><circle cx="12" cy="11" r="3"/><path d="M4 28h16"/></svg>
        <p>Daniel Moreno<br>Keystone Learning Company, Inc.<br>1200 Harbor Crest Drive Suite 310<br>Costa Verde, CA 92000</p>
      </div>
      <div class="tail"></div>
    </footer>
  </article>
</body>
</html>
```